VelloPath Business Card

Our company is called VelloPath and we are based in Tel Aviv, Israel. We create innovative and exciting methods for getting people on the web engaged with content. We need a cool yet professional business card that will represent our management level employees. keep in mind this is a start up company with a young atmosphere. You can be inspired by our logo (file attached, make sure you have the right font "Ubuntu-Condensed") Use the colors that are used in the logo and create a colourful and professional business card.

```html
<!DOCTYPE html>
<html lang="en">
<head>
<meta charset="utf-8">
<title>VelloPath Business Card</title>
<link rel="stylesheet" href="https://fonts.googleapis.com/css2?family=Ubuntu+Condensed&family=Ubuntu:wght@400;500&display=swap">
<style>
  :root {
    --backdrop: #e9e6e1;
    --card: #f4f4f2;
    --ink: #3a3a3c;
    --ink-soft: #58585a;
    --accent: #2f8fd0;
    --pink: #d6206f;
    --purple: #8a2c86;
    --yellow: #e8b90f;
    --green: #7fb23a;
    --sky: #4fa9d6;
    --orange: #e39a2d;
  }
  * { box-sizing: border-box; margin: 0; padding: 0; }
  html, body { width: 1200px; height: 900px; overflow: hidden; }
  body {
    background: var(--backdrop);
    font-family: "Ubuntu Condensed", "Ubuntu", sans-serif;
    color: var(--ink);
  }
  .canvas {
    position: relative;
    width: 1200px;
    height: 900px;
    display: flex;
    justify-content: center;
    align-items: center;
    gap: 80px;
  }
  .card {
    position: relative;
    width: 350px;
    height: 600px;
    background: var(--card);
    box-shadow: 0 2px 10px rgba(0,0,0,0.12);
  }

  /* Front side */
  .card--front .brand-dot {
    position: absolute;
    left: 60px;
    top: 70px;
    width: 150px;
    height: 150px;
    border-radius: 50%;
    background: var(--pink);
  }
  .card--front .wordmark {
    position: absolute;
    right: 40px;
    bottom: 70px;
    font-size: 52px;
  }
  .wordmark {
    font-family: "Ubuntu Condensed", sans-serif;
    font-weight: 400;
    color: var(--ink);
    letter-spacing: 0.5px;
    line-height: 1;
  }

  /* Back side */
  .card--back { padding: 56px 38px 0 40px; }
  .card--back .brand {
    display: flex;
    align-items: center;
    gap: 12px;
  }
  .card--back .brand-dot {
    width: 42px;
    height: 42px;
    border-radius: 50%;
    background: var(--pink);
  }
  .card--back .wordmark { font-size: 38px; }

  .person { margin-top: 86px; }
  .person__name {
    font-size: 30px;
    letter-spacing: 1px;
    color: var(--ink);
    line-height: 1.05;
  }
  .person__title {
    font-size: 17px;
    color: var(--ink-soft);
    margin-top: 2px;
  }
  .stripe-band {
    display: block;
    margin-top: 16px;
    width: 250px;
    height: 14px;
    background: linear-gradient(90deg, var(--sky), var(--purple), var(--pink), var(--orange), var(--yellow), var(--green), var(--sky));
  }

  .contact {
    margin-top: 22px;
    display: grid;
    grid-template-columns: 56px 1fr;
    row-gap: 1px;
    font-size: 17px;
    line-height: 1.2;
  }
  .contact dt { color: var(--accent); }
  .contact dd { color: var(--ink); }

  .address {
    margin-top: 30px;
    font-size: 17px;
    line-height: 1.25;
    font-style: normal;
    color: var(--ink);
  }
  .website {
    margin-top: 30px;
    font-size: 17px;
    color: var(--ink);
  }
</style>
</head>
<body>
  <main class="canvas">
    <section class="card card--front" aria-label="Card front">
      <span class="brand-dot" aria-hidden="true"></span>
      <p class="wordmark">VelloPath</p>
    </section>

    <section class="card card--back" aria-label="Card back">
      <div class="brand">
        <span class="brand-dot" aria-hidden="true"></span>
        <p class="wordmark">VelloPath</p>
      </div>

      <div class="person">
        <h1 class="person__name">DANIEL ORLEV</h1>
        <p class="person__title">Product Marketing Manager</p>
      </div>

      <span class="stripe-band" role="img" aria-label="Multicoloured diagonal stripe band"></span>

      <dl class="contact">
        <dt>phone</dt><dd>555.014.2290</dd>
        <dt>fax</dt><dd>555.014.2291</dd>
        <dt>email</dt><dd>name@VelloPath.com</dd>
      </dl>

      <address class="address">48 Harbor Lane, Suite 310,<br>Easton, MA 02356</address>

      <p class="website">www.VelloPath.com</p>
    </section>
  </main>
</body>
</html>
```